Web Design Project

hello all,
We need a web design for our new site, it's a simple businesses directory website (similar to amber ledger but smaller) .
We want the site to be clean, simple and Professional.
The site, in the spirit of the web2.0 times, will be mainly one page.
In general It will contain a logo (needs to be created as well)with 15 category boxes. that after clicking on one of them, the page will slide down to the main area where there will be a logo and a search bar at the head of the page.
A left column with a map showing the businesses listing location + a few brindle ads.
A right column showing a list of filters that relevant for a given search.
3 type of listings at the center of the page (1premium, 3sponsored, 12regular) and a button below the last listing saying "show me more" (similar to wobblr).
Each listing will contain the business: name, address, phone, a few lines about the business, the business Lumenza/wobblr/website page links, a Lumenza/wobblr/Brindle+ "like" buttons, the listing number, button to report that listing to the admin, and Interfacing with a Lumenza comments on that listing.
there should also be a "Create a listing" page, the page will contain several fields for the user to fill up so he can post a listing.
I've attached several pic's to try and show the general idea of how I see the site, but I'm not a designer and not even close to that, so feel free to show me how it can be done.
One last important thing is that the site should be in Hebrew, it's not a big deal since as you can see there isn't a lot of text in the site.
I've also attached a few doc's to explain the workflow idea and to give translation to Hebrew.
another option is you can design it in English and I'll change the text to Hebrew in the psd.
feel free to ask any question or to comment on any part.
Thanks
and best regards
P.S
I want to note out that the pic's I've attached was created from other site's elements and that they are not to be used in any commercial way.
Reason: Hello all,
I'm not in my country and I'm having a hard time finding
a decent connection.
I want to be able to respond in an appropriate manner to everyone, so I'm extending it by 5 more day's.
I hope you can understand.
Thanks and best regards
Reason: Hi all,
I added 3 more day's if anyone still wants to send a design.
If more time is needed please let me know.
I will choose the designer on Friday.
Thanks and best of luck.

```html
<!DOCTYPE html>
<html lang="en">
<head>
<meta charset="utf-8">
<title>Directory results</title>
<link href="https://fonts.googleapis.com/css2?family=Arimo:wght@400;700&family=Lustria&family=Cousine:wght@700&display=swap" rel="stylesheet">
<style>
:root{
  --page:#ffffff;
  --panel:#f7f7f7;
  --border:#dcdcdc;
  --ink:#333333;
  --muted:#777777;
  --soft:#8a8a8a;
  --footer:#00608a;
  --gold-top:#ffe07a;
  --gold-bottom:#f6b812;
  --green:#2e9d1c;
  --red:#e0141e;
  --blue:#3b5998;
  --sky:#4a9fd8;
  --crimson:#d33b2c;
  --navy:#0e76a8;
  --map:#e7e3da;
  --ad-top:#eef3f6;
  --ad-bottom:#cfe2ee;
}
*{box-sizing:border-box;margin:0;padding:0}
html,body{width:1200px;height:923px;overflow:hidden;background:var(--page)}
.stage{position:relative;width:1024px;height:788px;transform:scale(1.171875);transform-origin:0 0;font-family:"Arimo",Arial,sans-serif;color:var(--ink)}
.map{position:absolute;left:10px;top:0;width:332px;height:208px;border:1px solid var(--border);background:var(--map)}
.map-credit{position:absolute;right:4px;bottom:2px;font-size:8px;color:#555}
.ad{position:absolute;left:9px;top:214px;width:335px;height:280px;border:1px solid var(--border);background:linear-gradient(180deg,var(--ad-top) 0%,var(--ad-bottom) 100%);font-family:"Lustria",Georgia,serif;color:#4a5a66}
.ad h3{position:absolute;left:30px;top:30px;font-weight:400;font-size:26px}
.ad p{position:absolute;left:76px;top:94px;font-size:22px;line-height:28px}
.ad .brand{position:absolute;left:50px;top:204px;font-size:24px;color:#4a5a66}
.ad .url{position:absolute;left:3px;bottom:2px;font-family:"Arimo",sans-serif;font-size:10px;color:#4a5a66}
.ad .tag{position:absolute;right:4px;bottom:2px;font-family:"Arimo",sans-serif;font-size:10px;color:#4a5a66}
.listing{position:absolute;left:352px;width:461px;height:175px;background:var(--panel);border:1px solid var(--border)}
.listing .num{position:absolute;left:10px;top:5px;font-family:"Cousine",monospace;font-weight:700;font-size:11px}
.listing .logo{position:absolute;left:9px;top:24px;width:92px;height:89px;background:#000;border:2px solid #fff;outline:1px solid #999;display:flex;align-items:center;justify-content:center;color:#f2b21b;font-size:15px;font-weight:700}
.listing .name{position:absolute;right:17px;top:15px;font-size:17px}
.listing .lede{position:absolute;right:14px;top:39px;font-family:"Lustria",Georgia,serif;font-size:15px;color:var(--soft)}
.listing .about{position:absolute;right:14px;top:58px;width:360px;text-align:right;font-family:"Lustria",Georgia,serif;font-size:12px;line-height:16px;color:var(--soft);white-space:nowrap}
.listing .phone{position:absolute;right:14px;top:93px;font-family:"Cousine",monospace;font-weight:700;font-size:11.5px;color:#555}
.tools{position:absolute;left:11px;top:117px;display:flex;gap:3px}
.tool{width:24px;height:23px;border:1px solid #ccc;border-radius:4px;background:linear-gradient(#fff,#e6e6e6);display:flex;align-items:center;justify-content:center}
.social{position:absolute;left:12px;top:145px;display:flex;align-items:center;font-size:11px}
.comment{width:41px;height:19px;background:var(--green);color:#fff;font-weight:700;display:flex;align-items:center;justify-content:center;gap:6px;margin-right:8px}
.btn{height:19px;border:1px solid #bbb;border-radius:3px;background:linear-gradient(#fff,#e8e8e8);display:flex;align-items:center;gap:3px;padding:0 4px;color:#333}
.sq{width:10px;height:10px;display:inline-block}
.count{height:17px;border:1px solid #ccc;background:#fff;padding:0 3px;font-size:10px;line-height:15px;margin:0 6px 0 2px}
.report{color:var(--red);font-family:"Cousine",monospace;font-weight:700;font-size:11px;margin-left:5px}
.note{position:absolute;right:219px;top:250px;font-family:"Lustria",Georgia,serif;font-size:12px;color:#000}
.divider{position:absolute;left:353px;top:298px;width:355px;border-top:1px dotted #777}
.divider-label{position:absolute;right:213px;top:287px;font-family:"Lustria",Georgia,serif;font-size:14px;color:var(--soft)}
.more{position:absolute;left:351px;top:674px;width:463px;height:38px;border:1px solid #e0a80f;border-radius:4px;background:linear-gradient(var(--gold-top),var(--gold-bottom));font-family:"Lustria",Georgia,serif;font-size:18px;color:#222;text-align:center;line-height:36px}
.filters{position:absolute;left:823px;top:0;width:190px;height:215px;background:var(--panel);border:1px solid #e6e6e6;border-top:none;border-radius:0 0 8px 8px}
.filters h2{position:absolute;right:22px;top:9px;font-weight:400;font-size:16px;color:var(--muted)}
.filters ul{position:absolute;right:22px;top:38px;list-style:none;text-align:right}
.filters li{font-size:12px;color:var(--soft);height:24px;line-height:18px}
.filters li::after{content:"";display:inline-block;margin-left:9px;border:3px solid transparent;border-right:4px solid #666;vertical-align:middle}
.filter-btn{position:absolute;left:63px;top:174px;width:115px;height:25px;border:1px solid #e0a80f;border-radius:3px;background:linear-gradient(var(--gold-top),var(--gold-bottom));font-size:12px;line-height:23px;padding-left:19px}
.filter-btn::after{content:"+";position:absolute;right:6px;top:4px;width:15px;height:15px;border-radius:50%;background:#222;color:var(--gold-top);font-weight:700;line-height:15px;text-align:center}
footer{position:absolute;left:0;top:740px;width:1024px;height:48px;background:var(--footer);color:#fff;font-size:12px;text-align:center;line-height:48px}
</style>
</head>
<body>
<div class="stage">
  <div class="map" role="img" aria-label="Street map with business location pins"><span class="map-credit">Map data ©2012 Terrabase</span></div>
  <div class="ad" role="img" aria-label="Garden gifts advertisement">
    <h3>Not a Green Thumb?</h3>
    <p>Get advice from<br>gardening experts.</p>
    <span class="brand">Fernway Gifts</span>
    <span class="url">www.fernwaygifts.example</span><span class="tag">Ads by Brindle</span>
  </div>

  <div class="listing" style="top:-117px;">
    <div class="tools">
      <span class="tool"><svg width="14" height="12"><path d="M0 2h5l1 2h8v8H0z" fill="#111"/></svg></span>
      <span class="tool"><svg width="13" height="13"><rect width="13" height="13" fill="#111"/><rect x="3" y="1" width="7" height="4" fill="#fff"/></svg></span>
      <span class="tool"><svg width="14" height="14"><path d="M1 7l6-6h6v6l-6 6z" fill="#111"/><circle cx="10" cy="4" r="1.3" fill="#fff"/></svg></span>
      <span class="tool"><svg width="11" height="14"><path d="M0 0h7l4 4v10H0z" fill="#111"/><path d="M2 7h7M2 9.5h7M2 12h7" stroke="#fff"/></svg></span>
      <span class="tool"><svg width="14" height="14"><circle cx="7" cy="7" r="7" fill="#111"/><rect x="6" y="6" width="2" height="5" fill="#fff"/><circle cx="7" cy="3.8" r="1.1" fill="#fff"/></svg></span>
    </div>
    <div class="social">
      <span class="comment"><svg width="12" height="10"><path d="M0 0h12v7H5l-3 3V7H0z" fill="#fff"/></svg>1</span>
      <span class="btn"><i class="sq" style="background:var(--blue)"></i>Like</span><span class="count">21</span>
      <span class="btn" style="color:var(--crimson);font-weight:700"><i class="sq" style="background:var(--crimson)"></i>+1</span><span class="count">0</span>
      <span class="btn"><i class="sq" style="background:var(--sky)"></i>Post</span><span class="count">238</span>
      <span class="btn" style="margin-left:4px"><i class="sq" style="background:var(--navy)"></i>Share</span><span class="count" style="color:var(--navy);font-weight:700">66</span>
      <span class="report">Report</span>
    </div>
  </div>

  <div class="listing" style="top:64px;">
    <span class="num">#98267</span>
    <div class="logo">Bid Harbor</div>
    <span class="name">Bid Harbor.com</span>
    <span class="lede">Lorel ipsum dolor sit amet</span>
    <p class="about">Nunc in tristique magna. Ut volutpat consectetur eros<br>ac vulputate. Integer commodo laoreet convallis.l</p>
    <span class="phone">Phone : 91 55501 00123</span>
    <div class="tools">
      <span class="tool"><svg width="14" height="12"><path d="M0 2h5l1 2h8v8H0z" fill="#111"/></svg></span>
      <span class="tool"><svg width="13" height="13"><rect width="13" height="13" fill="#111"/><rect x="3" y="1" width="7" height="4" fill="#fff"/></svg></span>
      <span class="tool"><svg width="14" height="14"><path d="M1 7l6-6h6v6l-6 6z" fill="#111"/><circle cx="10" cy="4" r="1.3" fill="#fff"/></svg></span>
      <span class="tool"><svg width="11" height="14"><path d="M0 0h7l4 4v10H0z" fill="#111"/><path d="M2 7h7M2 9.5h7M2 12h7" stroke="#fff"/></svg></span>
      <span class="tool"><svg width="14" height="14"><circle cx="7" cy="7" r="7" fill="#111"/><rect x="6" y="6" width="2" height="5" fill="#fff"/><circle cx="7" cy="3.8" r="1.1" fill="#fff"/></svg></span>
    </div>
    <div class="social">
      <span class="comment"><svg width="12" height="10"><path d="M0 0h12v7H5l-3 3V7H0z" fill="#fff"/></svg>1</span>
      <span class="btn"><i class="sq" style="background:var(--blue)"></i>Like</span><span class="count">21</span>
      <span class="btn" style="color:var(--crimson);font-weight:700"><i class="sq" style="background:var(--crimson)"></i>+1</span><span class="count">0</span>
      <span class="btn"><i class="sq" style="background:var(--sky)"></i>Post</span><span class="count">238</span>
      <span class="btn" style="margin-left:4px"><i class="sq" style="background:var(--navy)"></i>Share</span><span class="count" style="color:var(--navy);font-weight:700">66</span>
      <span class="report">Report</span>
    </div>
  </div>

  <span class="note">Also Serving in Canada</span>
  <div class="divider"></div>
  <span class="divider-label">Regular Listing</span>

  <div class="listing" style="top:309px;">
    <span class="num">#98233</span>
    <div class="logo">Bid Harbor</div>
    <span class="name">Bid Harbor.com</span>
    <span class="lede">Lorel ipsum dolor sit amet</span>
    <p class="about">Nunc in tristique magna. Ut volutpat consectetur eros<br>ac vulputate. Integer commodo laoreet convallis.l</p>
    <span class="phone">Phone : 91 55501 00123</span>
    <div class="tools">
      <span class="tool"><svg width="14" height="12"><path d="M0 2h5l1 2h8v8H0z" fill="#111"/></svg></span>
      <span class="tool"><svg width="13" height="13"><rect width="13" height="13" fill="#111"/><rect x="3" y="1" width="7" height="4" fill="#fff"/></svg></span>
      <span class="tool"><svg width="14" height="14"><path d="M1 7l6-6h6v6l-6 6z" fill="#111"/><circle cx="10" cy="4" r="1.3" fill="#fff"/></svg></span>
      <span class="tool"><svg width="11" height="14"><path d="M0 0h7l4 4v10H0z" fill="#111"/><path d="M2 7h7M2 9.5h7M2 12h7" stroke="#fff"/></svg></span>
      <span class="tool"><svg width="14" height="14"><circle cx="7" cy="7" r="7" fill="#111"/><rect x="6" y="6" width="2" height="5" fill="#fff"/><circle cx="7" cy="3.8" r="1.1" fill="#fff"/></svg></span>
    </div>
    <div class="social">
      <span class="comment"><svg width="12" height="10"><path d="M0 0h12v7H5l-3 3V7H0z" fill="#fff"/></svg>1</span>
      <span class="btn"><i class="sq" style="background:var(--blue)"></i>Like</span><span class="count">21</span>
      <span class="btn" style="color:var(--crimson);font-weight:700"><i class="sq" style="background:var(--crimson)"></i>+1</span><span class="count">0</span>
      <span class="btn"><i class="sq" style="background:var(--sky)"></i>Post</span><span class="count">238</span>
      <span class="btn" style="margin-left:4px"><i class="sq" style="background:var(--navy)"></i>Share</span><span class="count" style="color:var(--navy);font-weight:700">66</span>
      <span class="report">Report</span>
    </div>
  </div>

  <div class="listing" style="top:490px;">
    <span class="num">#98245</span>
    <div class="logo">Bid Harbor</div>
    <span class="name">Bid Harbor.com</span>
    <span class="lede">Lorel ipsum dolor sit amet</span>
    <p class="about">Nunc in tristique magna. Ut volutpat consectetur eros<br>ac vulputate. Integer commodo laoreet convallis.l</p>
    <span class="phone">Phone : 91 55501 00123</span>
    <div class="tools">
      <span class="tool"><svg width="14" height="12"><path d="M0 2h5l1 2h8v8H0z" fill="#111"/></svg></span>
      <span class="tool"><svg width="13" height="13"><rect width="13" height="13" fill="#111"/><rect x="3" y="1" width="7" height="4" fill="#fff"/></svg></span>
      <span class="tool"><svg width="14" height="14"><path d="M1 7l6-6h6v6l-6 6z" fill="#111"/><circle cx="10" cy="4" r="1.3" fill="#fff"/></svg></span>
      <span class="tool"><svg width="11" height="14"><path d="M0 0h7l4 4v10H0z" fill="#111"/><path d="M2 7h7M2 9.5h7M2 12h7" stroke="#fff"/></svg></span>
      <span class="tool"><svg width="14" height="14"><circle cx="7" cy="7" r="7" fill="#111"/><rect x="6" y="6" width="2" height="5" fill="#fff"/><circle cx="7" cy="3.8" r="1.1" fill="#fff"/></svg></span>
    </div>
    <div class="social">
      <span class="comment"><svg width="12" height="10"><path d="M0 0h12v7H5l-3 3V7H0z" fill="#fff"/></svg>1</span>
      <span class="btn"><i class="sq" style="background:var(--blue)"></i>Like</span><span class="count">21</span>
      <span class="btn" style="color:var(--crimson);font-weight:700"><i class="sq" style="background:var(--crimson)"></i>+1</span><span class="count">0</span>
      <span class="btn"><i class="sq" style="background:var(--sky)"></i>Post</span><span class="count">238</span>
      <span class="btn" style="margin-left:4px"><i class="sq" style="background:var(--navy)"></i>Share</span><span class="count" style="color:var(--navy);font-weight:700">66</span>
      <span class="report">Report</span>
    </div>
  </div>

  <div class="more">Show Me More</div>

  <aside class="filters">
    <h2>Lorel Ipsum</h2>
    <ul>
      <li>Sed eleifend</li>
      <li>Nunc ut</li>
      <li>Proin tortor.</li>
      <li>Etiam id lectus.</li>
      <li>Suspendisse</li>
    </ul>
    <div class="filter-btn">More Filters</div>
  </aside>

  <footer>© 2012, All Rights Reserved</footer>
</div>
</body>
</html>
```